Packaging Sleeve Design for Yoghurt Tubs

Wagglenook makes frozen yoghurt treats for dogs. Our healthy treats are packaged like regular yoghurt in small tubs with a lid.

What we require is a design for our packaging using all the current logos and flavor icons we already have available.

The packaging will be a carton sleeve that wraps around the tubs.

We would like to maintain a wholesome / homemade look about the packaging following the design and look of our existing logo. You can visit the website www.wagglenook.com.au to get a better idea.

The packets will be displayed in a freezer so we would like something that will stand out to catch the customers eye.

Target Market(s)

Dog lovers, pet owners

Requirements
Must have
• Logo & flavours
All natural message
Low fat, low calories

```html
<!DOCTYPE html>
<html lang="en">
<head>
<meta charset="utf-8">
<title>Wagglenook – Nibbly Banana sleeve</title>
<link rel="stylesheet" href="https://fonts.googleapis.com/css2?family=Bebas+Neue&family=Dosis:wght@200;300;400&family=Short+Stack&display=swap">
<style>
  :root{
    --cream:#fdfbf1;
    --band:#fcf6d9;
    --white:#ffffff;
    --yellow:#f6cb2e;
    --yellow-soft:#fbe89a;
    --ink:#23262b;
    --ghost:#f1ede0;
  }
  *{margin:0;padding:0;box-sizing:border-box}
  html,body{width:1200px;height:1016px;overflow:hidden;background:var(--cream)}
  .sleeve{position:relative;width:1200px;height:1016px;background:var(--cream);overflow:hidden}
  .band{position:absolute;left:0;width:1200px;background:var(--band)}
  .band--top{top:0;height:20px}
  .band--bottom{bottom:0;height:28px}

  .fold{position:absolute;border-left:3px dotted var(--yellow)}
  .fold--left{left:276px;top:20px;height:968px}
  .fold--right{left:921px;top:20px;height:968px}
  .cut{position:absolute;border-top:3px dotted var(--yellow);height:0}

  /* front panel */
  .flavour{position:absolute;left:373px;top:100px;font-family:"Bebas Neue",sans-serif;color:var(--yellow);text-align:center}
  .flavour__name{font-size:58px;line-height:1;letter-spacing:1px}
  .flavour__kind{font-family:"Dosis",sans-serif;font-weight:400;font-size:17px;letter-spacing:1px;margin-top:-2px}
  .disc{position:absolute;left:372px;top:167px;width:456px;height:456px;border-radius:50%;background:var(--white)}
  .fruit-photo{position:absolute;left:440px;top:368px;width:330px;height:115px;border-radius:50% 50% 45% 45% / 30% 30% 70% 70%;background:radial-gradient(ellipse at 55% 60%,#f8d433 0%,#f3c21d 55%,#e9b21a 100%)}
  .nutrients{position:absolute;z-index:2;font-family:"Short Stack",cursive;color:var(--ink)}
  .nutrients__title{font-size:19px;line-height:1.2}
  .nutrients__list{list-style:none;font-family:"Dosis",sans-serif;font-weight:300;color:var(--yellow);font-size:21px;line-height:30px}
  .nutrients__list li::before{content:"• "}
  .nutrients--front{left:490px;top:213px}
  .front-note{position:absolute;left:500px;top:499px;width:145px;text-align:center;font-family:"Short Stack",cursive;font-size:18px;color:var(--ink)}

  .brand{position:absolute;left:440px;top:760px;width:320px;height:60px;display:flex;align-items:center;justify-content:center;gap:14px}
  .brand__dot{width:38px;height:38px;border-radius:50%;background:var(--ink)}
  .brand__name{font-family:"Bebas Neue",sans-serif;font-size:54px;color:var(--ink);letter-spacing:1px;line-height:1}

  .claims{font-family:"Bebas Neue",sans-serif;color:var(--ink);white-space:nowrap;letter-spacing:1px}
  .claims--front{position:absolute;left:0;width:1200px;top:942px;text-align:center;font-size:36px}

  /* side panels */
  .side{position:absolute;top:0;width:1016px;height:277px;transform-origin:0 0}
  .side--left{left:277px;transform:rotate(90deg)}
  .side--right{left:923px;top:1016px;transform:rotate(-90deg)}
  .side__hello{position:absolute;left:66px;top:36px;font-family:"Short Stack",cursive;font-size:38px;color:var(--ink);line-height:1}
  .side__natural{position:absolute;left:66px;top:96px;font-family:"Dosis",sans-serif;font-weight:200;font-size:50px;color:var(--yellow);line-height:1;letter-spacing:1px}
  .side__pets{position:absolute;left:66px;top:160px;font-family:"Short Stack",cursive;font-size:38px;color:var(--ink);line-height:1}
  .side__copy{position:absolute;left:52px;top:222px;width:400px;font-family:"Dosis",sans-serif;font-weight:400;font-size:13.5px;line-height:17px;color:var(--ink)}
  .side__claims{position:absolute;left:486px;top:230px;font-size:35px}
  .side__icon{position:absolute;left:600px;top:24px;width:170px;height:186px;border-radius:40% 60% 50% 50%;background:linear-gradient(135deg,var(--yellow-soft),#fff3c0)}
  .side__ghost{position:absolute;z-index:1;left:562px;top:40px;font-family:"Bebas Neue",sans-serif;font-size:54px;color:var(--ghost);line-height:1}
  .nutrients--side{left:815px;top:40px}
</style>
</head>
<body>
<main class="sleeve">
  <div class="band band--top"></div>
  <div class="band band--bottom"></div>

  <div class="fold fold--left"></div>
  <div class="fold fold--right"></div>
  <div class="cut" style="left:302px;top:160px;width:72px"></div>
  <div class="cut" style="left:772px;top:160px;width:128px"></div>
  <div class="cut" style="left:302px;top:695px;width:72px"></div>
  <div class="cut" style="left:760px;top:695px;width:140px"></div>

  <section class="side side--left">
    <p class="side__hello">Wholesome</p>
    <p class="side__natural">ALL NATURAL</p>
    <p class="side__pets">treats for pets.</p>
    <p class="side__copy">The Nibblys ingredients are ideal for muscle and blood vessel function. They protect cells from damage and help build cartilage.</p>
    <div class="side__icon" role="img" aria-label="Yellow outline banana flavour icon"></div>
    <p class="side__ghost">NIBBLY</p>
    <div class="nutrients nutrients--side">
      <p class="nutrients__title">high in</p>
      <ul class="nutrients__list"><li>potassium</li><li>magnesium</li><li>vitamin B6</li><li>vitamin C</li></ul>
    </div>
    <p class="claims side__claims">100% NATURAL - LOW FAT - LOW CALORIES</p>
  </section>

  <section class="side side--right">
    <p class="side__hello">Wholesome</p>
    <p class="side__natural">ALL NATURAL</p>
    <p class="side__pets">treats for pets.</p>
    <p class="side__copy">The Nibblys ingredients are ideal for muscle and blood vessel function. They protect cells from damage and help build cartilage.</p>
    <div class="side__icon" role="img" aria-label="Yellow outline banana flavour icon"></div>
    <p class="side__ghost">NIBBLY</p>
    <div class="nutrients nutrients--side">
      <p class="nutrients__title">high in</p>
      <ul class="nutrients__list"><li>potassium</li><li>magnesium</li><li>vitamin B6</li><li>vitamin C</li></ul>
    </div>
    <p class="claims side__claims">100% NATURAL - LOW FAT - LOW CALORIES</p>
  </section>

  <div class="flavour">
    <p class="flavour__name">NIBBLY</p>
    <p class="flavour__kind">{BANANA}</p>
  </div>
  <div class="disc"></div>
  <div class="fruit-photo" role="img" aria-label="Photograph of a ripe yellow banana"></div>
  <div class="nutrients nutrients--front">
    <p class="nutrients__title">high in</p>
    <ul class="nutrients__list"><li>potassium</li><li>magnesium</li><li>vitamin B6</li><li>vitamin C</li></ul>
  </div>
  <p class="front-note">all natural</p>

  <div class="brand">
    <span class="brand__dot"></span>
    <span class="brand__name">Wagglenook</span>
  </div>

  <p class="claims claims--front">100% NATURAL - LOW FAT - LOW CALORIES</p>
</main>
</body>
</html>
```